BargoStreet Landing Page

We need a landing page for BargoStreet, which is a Deal of the day website targeting and providing daily deals to college students. The information we need on the page is as follows:
-The BargoStreet logo
-Save 50% to 90% on Great Deals Near Your College Campus and Beyond
-Enter Your Information
Email:
Location:
And a Submit button
-The footer
-We’d like to see a reference to how to earn credits for inviting friends: We are offering $50 Wandervane gift card for 10 new invites or $5 BargoStreet dollars for each invite.
If you visit www.bargostreet.com/marketing you can see our current landing page with all of the information. If you have any questions, please contact Renata at RCorvallo@bargostreet.com
Updates
We will need a Photoshop version of the final design as well.
BargoStreet has made a change to their target market, and is no longer just targeting college students. We are expanding our target market ages: 18-50+. The majority of our members will be between the ages of 18-35, so please keep that in mind when you are editing your designs. I am very sorry for the inconvenience. I will be extending the end date so there is enough time to edit. Thank you and keep up the great work!

```html
<!DOCTYPE html>
<html lang="en">
<head>
<meta charset="utf-8">
<title>BargoStreet – Save 50% to 90% on Great Deals</title>
<link href="https://fonts.googleapis.com/css2?family=Gochi+Hand&family=Arimo:wght@400;700&display=swap" rel="stylesheet">
<style>
  :root {
    --page-bg: #e8eae9;
    --band-dark: #1f3f4f;
    --band-mid: #2c5366;
    --accent-green: #8bab3c;
    --accent-green-dark: #6d8f24;
    --ink: #1d3a4a;
    --white: #ffffff;
    --field-border: #c9cdcc;
    --card-blue: #1d4f8a;
    --photo-a: #3a4a52;
    --photo-b: #1c2a31;
  }
  * { box-sizing: border-box; margin: 0; padding: 0; }
  html, body { width: 1200px; height: 809px; overflow: hidden; }
  body {
    position: relative;
    background: radial-gradient(ellipse at 50% 0%, #f6f7f7 0%, var(--page-bg) 60%);
    font-family: "Arimo", Arial, sans-serif;
    color: var(--ink);
  }
  .hero-band { position: absolute; left: 0; top: 0; width: 1200px; height: 809px; }

  .brand {
    position: absolute; display: flex; align-items: center; gap: 10px;
    font-family: "Arimo", Arial, sans-serif; font-weight: 700; color: var(--ink);
  }
  .brand-mark { background: var(--accent-green); }
  .brand--header { left: 84px; top: 46px; font-size: 50px; }
  .brand--header .brand-mark { width: 26px; height: 26px; }
  .brand--footer { left: 934px; top: 712px; font-size: 28px; }
  .brand--footer .brand-mark { width: 16px; height: 16px; }

  .student-photo {
    position: absolute; left: 44px; top: 160px; width: 506px; height: 528px;
    background: radial-gradient(ellipse at 50% 45%, var(--photo-a) 0%, var(--photo-b) 75%);
    border-radius: 200px 200px 40px 60px;
  }

  .signup { position: absolute; left: 588px; top: 205px; }
  .signup-title {
    font-family: "Gochi Hand", cursive; color: var(--white);
    font-size: 40px; font-weight: 400; line-height: 1; white-space: nowrap;
  }
  .signup-subtitle {
    font-family: "Gochi Hand", cursive; color: var(--white);
    font-size: 30px; font-weight: 400; margin-top: 10px; white-space: nowrap;
  }
  .signup-label {
    color: var(--accent-green); font-weight: 700; font-size: 19px; margin-top: 22px;
  }
  .field {
    display: flex; align-items: center; justify-content: space-between;
    width: 240px; height: 42px; margin-top: 12px; padding: 0 12px;
    background: linear-gradient(#ffffff, #eef0ef);
    border: 3px solid var(--field-border); border-radius: 8px;
    font-size: 17px; color: #222;
  }
  .field + .field { margin-top: 18px; }
  .field-arrows { font-size: 9px; line-height: 8px; color: #333; text-align: center; }
  .submit-button {
    display: block; margin-top: 16px; width: 122px; height: 36px;
    border: none; border-radius: 18px;
    background: linear-gradient(#9cbc4a, var(--accent-green-dark));
    color: var(--white); font-family: "Gochi Hand", cursive; font-size: 22px;
  }

  .reward { position: absolute; top: 528px; width: 114px; }
  .reward--gift { left: 590px; }
  .reward--credit { left: 715px; }
  .reward-card {
    height: 68px; border: 3px solid var(--white); border-radius: 6px;
    position: relative; color: var(--white);
  }
  .reward--gift .reward-card { background: linear-gradient(135deg, #2a64a6, var(--card-blue)); }
  .reward--credit .reward-card { background: linear-gradient(135deg, #ffffff 55%, #e5e8e6); color: var(--ink); }
  .reward-brand { position: absolute; right: 8px; top: 10px; font-size: 11px; font-weight: 700; }
  .reward--credit .reward-brand { left: 10px; right: auto; top: 38px; font-size: 11px; }
  .reward-amount { position: absolute; right: 8px; bottom: 6px; font-size: 19px; }
  .reward--credit .reward-amount {
    left: 0; top: 0; right: auto; bottom: auto; width: 100%; height: 26px;
    background: var(--accent-green); color: var(--white); font-size: 15px; padding: 4px 8px;
  }
  .reward-note { font-size: 10px; color: var(--white); margin-top: 6px; padding-left: 4px; }

  .site-footer { position: absolute; left: 84px; top: 712px; display: flex; font-size: 14px; line-height: 17.5px; }
  .footer-col { list-style: none; }
  .footer-col:nth-child(1) { width: 145px; }
  .footer-col:nth-child(2) { width: 192px; }
  .footer-col:nth-child(3) { width: 132px; }
  .footer-col:nth-child(4) { width: 144px; }
  .footer-col--contact li { display: flex; align-items: center; gap: 8px; margin-bottom: 6px; line-height: 18px; }
  .contact-icon { width: 18px; height: 18px; flex: none; }
  .copyright { position: absolute; left: 978px; top: 764px; font-size: 14px; }
</style>
</head>
<body>
  <svg class="hero-band" viewBox="0 0 1200 809" aria-hidden="true">
    <defs>
      <linearGradient id="bandShade" x1="0" y1="0" x2="1" y2="1">
        <stop offset="0" stop-color="var(--band-mid)"/>
        <stop offset="1" stop-color="var(--band-dark)"/>
      </linearGradient>
    </defs>
    <polygon fill="var(--accent-green)"
      points="0,206 206,178 214,128 238,172 1200,70 1200,84 240,186 216,148 210,192 0,222"/>
    <polygon fill="url(#bandShade)"
      points="0,222 210,192 216,148 240,186 1200,84 1200,626 0,626"/>
    <rect x="0" y="626" width="1200" height="16" fill="var(--accent-green)"/>
  </svg>

  <div class="brand brand--header"><span class="brand-mark"></span>BargoStreet</div>

  <div class="student-photo" role="img" aria-label="Photo of a smiling student sitting cross-legged holding books, with a backpack beside her"></div>

  <form class="signup">
    <h1 class="signup-title">Save 50% to 90% on Great Deals</h1>
    <h2 class="signup-subtitle">Near Your College Campus and Beyond</h2>
    <p class="signup-label">Enter Your Information</p>
    <div class="field">Email</div>
    <div class="field">select location <span class="field-arrows">▲<br>▼</span></div>
    <button class="submit-button" type="button">SUBMIT</button>
  </form>

  <div class="reward reward--gift">
    <div class="reward-card"><span class="reward-brand">Wandervane</span><span class="reward-amount">$50</span></div>
    <p class="reward-note">*for 10 new invites</p>
  </div>
  <div class="reward reward--credit">
    <div class="reward-card"><span class="reward-amount">$5</span><span class="reward-brand">BargoStreet</span></div>
    <p class="reward-note">*for each invite</p>
  </div>

  <footer class="site-footer">
    <ul class="footer-col"><li>Daily Deal</li><li>Recent Deals</li><li>How It Works</li><li>Submit Business</li></ul>
    <ul class="footer-col"><li>Feedback</li><li>Sign Up</li><li>Feature Your Business</li></ul>
    <ul class="footer-col"><li>FAQs</li><li>About Us</li><li>Contact Us</li></ul>
    <ul class="footer-col"><li>Legal</li><li>Our Promise</li><li>We're Hiring</li></ul>
    <ul class="footer-col footer-col--contact">
      <li><svg class="contact-icon" viewBox="0 0 18 18"><rect x="1" y="4" width="16" height="11" fill="#fff" stroke="#9aa3a6"/><path d="M1 4 L9 10 L17 4" fill="none" stroke="#9aa3a6"/></svg>Contact us via Email</li>
      <li><svg class="contact-icon" viewBox="0 0 18 18"><rect x="1" y="1" width="16" height="16" rx="2" fill="#3b5b8c"/></svg>Join on Friendwall</li>
      <li><svg class="contact-icon" viewBox="0 0 18 18"><rect x="1" y="1" width="16" height="16" rx="2" fill="#4aa6d6"/></svg>Follow us on Chirpline</li>
    </ul>
  </footer>

  <div class="brand brand--footer"><span class="brand-mark"></span>BargoStreet</div>
  <p class="copyright">© 2011 | BargoStreet.</p>
</body>
</html>
```